Organic rose water based skincare line in need of product label and packaging design

We are looking for a simple, clean, modern labeling and packaging design for 2 of our products. Our brand's demographic is upscale females ages 20-40. We want our packaging to be very minimalistic, and instagramable.

Product #1: Rose water facial spray "Lumi Mist"
Product #2: Rose water facial toner "Velvet Hush Hour"

Please see attached images for our current logo and label design. We have also added some images that inspire our branding.

Target Market(s)

trendy woman ages 20-40

Industry/Entity Type

Skin Care Product

Font styles to use
Serif
Sans Serif

Colors

Designer to choose only greyscale colors for use in the design.

Requirements
Must have
• Must have our logo, bottle size, product name on front and how to use and ingredient on the back. Please see project description and attached images for more information.
Should not have
• Too much going on or too many colors.

```html
<!DOCTYPE html>
<html lang="en">
<head>
<meta charset="UTF-8">
<title>the petal co. — Velvet Hush Hour &amp; Lumi Mist</title>
<link rel="stylesheet" href="https://fonts.googleapis.com/css2?family=Urbanist:wght@300;400;500&display=swap">
<style>
  :root {
    --backdrop: #dcdcdb;
    --tube-body: #e6e6e4;
    --cap: #262626;
    --box-light: #d9d9d7;
    --box-dark: #232323;
    --ink: #1d1d1d;
    --ink-soft: #6a6a6a;
    --paper: #ffffff;
  }
  * { margin: 0; padding: 0; box-sizing: border-box; }
  html, body { width: 1200px; height: 1200px; overflow: hidden; }
  body {
    background: var(--backdrop);
    font-family: "Urbanist", sans-serif;
    position: relative;
  }

  /* Toner tube label, laid flat */
  .tube {
    position: absolute;
    left: 388px; top: 346px;
    width: 179px; height: 458px;
  }
  .tube-body {
    position: absolute; left: 0; top: 0;
    width: 179px; height: 391px;
    background: var(--tube-body);
    text-align: center;
    color: var(--ink);
  }
  .tube-cap {
    position: absolute; left: 35px; top: 391px;
    width: 109px; height: 67px;
    background: var(--cap);
    border-radius: 0 0 6px 6px;
  }
  .tube .brand {
    position: absolute; left: 0; right: 0; top: 36px;
    font-size: 17px; font-weight: 400; letter-spacing: 0.2px;
  }
  .tube .product-name {
    position: absolute; left: 0; right: 0; top: 168px;
    font-size: 24px; font-weight: 300; line-height: 31px;
    letter-spacing: 0.5px;
  }
  .tube .descriptor {
    position: absolute; left: 0; right: 0; top: 268px;
    font-size: 7.5px; font-weight: 300; color: var(--ink-soft);
  }
  .tube .volume {
    position: absolute; left: 0; right: 0; top: 280px;
    font-size: 6px; font-weight: 500;
  }

  /* Mist box front panel */
  .box {
    position: absolute;
    left: 584px; top: 469px;
    width: 195px; height: 473px;
    text-align: center;
  }
  .box-upper {
    position: absolute; left: 0; top: 0;
    width: 195px; height: 300px;
    background: var(--box-light);
    color: var(--ink);
  }
  .box-lower {
    position: absolute; left: 0; top: 300px;
    width: 195px; height: 173px;
    background: var(--box-dark);
    color: var(--paper);
  }
  .box .brand {
    position: absolute; left: 0; right: 0; top: 34px;
    font-size: 18px; font-weight: 500; color: var(--paper);
  }
  .box .directions {
    position: absolute; left: 0; right: 0; top: 96px;
    font-size: 8.5px; font-weight: 500; line-height: 11px;
  }
  .box .ingredients {
    position: absolute; left: 0; right: 0; top: 165px;
    font-size: 12.5px; font-weight: 500;
  }
  .box .benefits {
    position: absolute; left: 0; right: 0; top: 191px;
    list-style: none;
    font-size: 8px; font-weight: 300; line-height: 11px;
    color: var(--ink-soft);
  }
  .box .product-name {
    position: absolute; left: 0; right: 0; top: 10px;
    font-size: 38px; font-weight: 400; line-height: 46px;
  }
  .box .descriptor {
    position: absolute; left: 0; right: 0; top: 110px;
    font-size: 9px; font-weight: 300; line-height: 11px;
  }
  .box .volume {
    position: absolute; left: 0; right: 0; top: 143px;
    font-size: 9px; font-weight: 400;
  }
</style>
</head>
<body>
  <section class="tube" aria-label="Velvet Hush Hour toner tube">
    <div class="tube-body">
      <p class="brand">the petal co.</p>
      <h1 class="product-name">VELVET<br>HUSH<br>HOUR</h1>
      <p class="descriptor">organic rose facial toner</p>
      <p class="volume">4 oz / 120 mL</p>
    </div>
    <div class="tube-cap"></div>
  </section>

  <section class="box" aria-label="Lumi Mist box">
    <div class="box-upper">
      <p class="brand">the petal co.</p>
      <p class="directions">shake well.<br>apply a small amount of<br>toner to a clean cotton pad<br>+ gently sweep over your<br>face + neck</p>
      <p class="ingredients">witchhazel/rose</p>
      <ul class="benefits">
        <li>+ tightens skin</li>
        <li>+ shrinks pores</li>
        <li>+ prevents acne</li>
        <li>+ treats discoloration</li>
        <li>+ removes impurities</li>
      </ul>
    </div>
    <div class="box-lower">
      <h2 class="product-name">LUMI<br>MIST</h2>
      <p class="descriptor">Organic rosewater<br>hydrating mist</p>
      <p class="volume">2 oz / 60mL</p>
    </div>
  </section>
</body>
</html>
```